App UI design needed! For a Quendly Management Tool

Need a design of a Windows desktop application which is a Quendly Management Tool, similar to Vaultrixa, Kelmorin or Tibruna, with Business/Enterprise functionalities. Here attached are a few sample pages of Kelmorin, and some sample pages of our app called Quendly. We certainly want to redesign our app.
We need: 1. The layout of the web: top banner, menu, main pane; 2. Form style, main form and sub forms; 3. List style; 4 Fonts and buttons; 5. Logo.
The design should look professional, can attract business customers as well as individual users, and present a strong sense of “Security”. The look and feel should differentiate from well-known products like Vaultrixa, Kelmorin, Tibruna, etc.

```html
<!DOCTYPE html>
<html lang="en">
<head>
<meta charset="utf-8">
<title>Quendly – Passwords</title>
<link href="https://fonts.googleapis.com/css2?family=Barlow:wght@400;500;600;700;800&display=swap" rel="stylesheet">
<style>
:root{
  --plum-night:#2c0838;
  --plum-deep:#47105a;
  --plum:#5b1a70;
  --plum-mid:#6c2488;
  --violet:#8a2aa8;
  --magenta:#c23fd8;
  --lilac-band:#f2dcf8;
  --lilac-soft:#f6e8fa;
  --lilac-btn:#e5c8f2;
  --card-border:#e6b9ee;
  --white:#ffffff;
  --ink:#1d1d1d;
  --ink-soft:#444;
  --row-grey:#f2f2f2;
  --side-grey:#f3f3f3;
  --rule:#d6d6d6;
  --danger:#e0161e;
  --black:#000;
  --chirp:#4a9fe8;
  --friend:#1c59b3;
}
*{box-sizing:border-box;margin:0;padding:0}
html,body{width:1200px;height:816px;overflow:hidden;background:var(--white)}
body{font-family:"Barlow",sans-serif;color:var(--ink);position:relative}
.abs{position:absolute}
.top-strip{left:0;top:0;width:1200px;height:36px;background:var(--plum-night)}
.header{left:0;top:36px;width:1200px;height:73px;background:var(--plum-deep)}
.brand{left:0;top:0;width:270px;height:73px;background:var(--white);display:flex;align-items:center;padding-left:62px}
.brand-name{font-weight:800;font-size:21px;letter-spacing:2px;color:var(--plum-night)}
.welcome{left:270px;top:0;width:224px;height:73px;background:var(--plum);color:var(--white);font-size:16px;display:flex;align-items:center;padding-left:31px}
.switch-label{left:526px;top:27px;font-size:13px;color:var(--magenta)}
.switch{left:613px;top:17px;width:353px;height:37px;border-radius:19px;background:var(--white);display:flex;align-items:center;font-size:13px;color:var(--plum)}
.switch .on{width:102px;height:33px;margin-left:2px;border-radius:17px;background:var(--plum);color:var(--white);display:flex;align-items:center;justify-content:center}
.switch span{margin-left:28px}
.avatar{left:1094px;top:16px;width:40px;height:40px;border-radius:50%;background:var(--white);border:3px solid var(--lilac-btn);display:flex;align-items:center;justify-content:center;font-weight:700;font-size:16px}
.dots{width:4px;display:flex;flex-direction:column;gap:4px}
.dots i{width:4px;height:4px;border-radius:50%;background:var(--white);display:block}
.category-band{left:0;top:109px;width:1200px;height:198px;background:var(--lilac-band)}
.cat{background:var(--white);border:1px solid var(--card-border);border-radius:3px;display:flex;flex-direction:column;align-items:center;justify-content:center;gap:10px;font-size:12px;color:var(--ink-soft)}
.cat svg{width:26px;height:26px}
.cat.active{box-shadow:0 3px 10px rgba(90,26,112,.25);font-size:18px;color:var(--plum);font-weight:500}
.see-all{left:682px;top:69px;width:61px;height:69px;background:var(--lilac-btn);border-radius:3px;font-size:12px;color:var(--ink);display:flex;flex-direction:column;align-items:center;justify-content:center;gap:6px}
.promo{left:758px;top:29px;width:408px;height:142px;background:linear-gradient(100deg,#5b1a8a,#3b2c8c 45%,#2f4a9a);}
.promo-dots{left:954px;top:178px;display:flex;gap:3px}
.promo-dots i{width:4px;height:4px;border-radius:50%;background:#b9b9c9;display:block}
.promo-dots i:first-child{background:#555}
.toolbar{left:0;top:307px;width:1200px;height:75px;background:var(--plum-deep)}
.tabs{left:28px;top:18px;width:203px;height:38px;border-radius:19px;background:var(--white);display:flex;align-items:center;font-size:13px;font-weight:500}
.tabs .on{width:100px;height:34px;margin-left:2px;border-radius:17px;background:var(--plum);color:var(--white);display:flex;align-items:center;justify-content:center}
.tabs span{margin-left:34px;color:var(--plum)}
.search-zone{left:270px;top:0;width:317px;height:75px;background:var(--white)}
.search{left:19px;top:18px;width:235px;height:40px;border-radius:20px;border:1px solid #d9c4e2;background:#faf6fb;display:flex;align-items:center;justify-content:space-between;padding:0 20px;font-size:12px;color:#777}
.add-btn{left:608px;top:20px;width:209px;height:38px;border-radius:3px;background:var(--plum-mid);color:var(--white);font-size:16px;font-weight:500;display:flex;align-items:center;gap:12px;padding-left:14px}
.sidebar{left:0;top:382px;width:270px;height:434px;background:var(--side-grey);border-right:1px solid #e2e2e2}
.tool{left:22px;width:224px;height:51px;border-bottom:1px solid var(--rule);display:flex;align-items:center;gap:14px;padding-left:14px;font-size:12px;font-weight:500}
.tool.first{font-weight:700}
.tool svg{width:16px;height:16px}
.table-head{left:270px;top:382px;width:930px;height:50px;background:var(--lilac-soft);font-size:15px;font-weight:500}
.row{left:270px;width:930px;font-size:12px;font-weight:500}
.cell{position:absolute}
.mark{width:24px;height:24px;border-radius:3px}
.btn{height:35px;border-radius:3px;font-size:12px;display:flex;align-items:center;justify-content:center}
.view-menu{left:1045px;top:364px;width:138px;height:105px;background:var(--white);border-radius:3px;box-shadow:0 2px 8px rgba(0,0,0,.18);font-size:12px}
.view-item{left:18px;display:flex;align-items:center;gap:12px}
</style>
</head>
<body>
<div class="abs top-strip"></div>

<header class="abs header">
  <div class="abs brand"><span class="brand-name">Quendly</span></div>
  <div class="abs welcome">Welcome Back Remy!</div>
  <div class="abs switch-label">Switch user ›</div>
  <div class="abs switch"><div class="on">Personal</div><span>SecurityHUB</span><span style="margin-left:20px">|&nbsp;&nbsp; My child (Remy)</span></div>
  <div class="abs avatar">R</div>
  <div class="abs dots" style="left:1164px;top:25px"><i></i><i></i><i></i></div>
</header>

<section class="abs category-band">
  <div class="abs cat active" style="left:28px;top:49px;width:110px;height:112px">
    <svg viewBox="0 0 26 26"><rect x="2" y="14" width="22" height="9" fill="#f1d4f7"/><rect x="7" y="10" width="12" height="10" rx="1" fill="#6c2488"/><path d="M9.5 10V7a3.5 3.5 0 0 1 7 0v3" fill="none" stroke="#6c2488" stroke-width="2"/></svg>
    Passwords</div>
  <div class="abs cat" style="left:149px;top:55px;width:95px;height:98px">
    <svg viewBox="0 0 26 26"><rect x="5" y="4" width="16" height="18" rx="2" fill="#dd88ef"/><path d="M9 10h8M9 13.5h8M9 17h5" stroke="#fff" stroke-width="1.6"/></svg>Secure Notes</div>
  <div class="abs cat" style="left:253px;top:55px;width:96px;height:98px">
    <svg viewBox="0 0 26 26"><rect x="3" y="6" width="20" height="14" rx="2" fill="none" stroke="#dd88ef" stroke-width="2"/><path d="M3 11h20" stroke="#dd88ef" stroke-width="2"/></svg>Credit Cards</div>
  <div class="abs cat" style="left:358px;top:55px;width:95px;height:98px">
    <svg viewBox="0 0 26 26"><circle cx="13" cy="9" r="4.5" fill="none" stroke="#dd88ef" stroke-width="2"/><path d="M4 22a9 7 0 0 1 18 0z" fill="none" stroke="#dd88ef" stroke-width="2"/></svg>Personal Info</div>
  <div class="abs cat" style="left:464px;top:55px;width:97px;height:98px">
    <svg viewBox="0 0 26 26"><rect x="4" y="6" width="18" height="15" rx="2" fill="#dd88ef"/><rect x="13" y="11" width="9" height="5" fill="#fff"/><circle cx="16" cy="13.5" r="1.3" fill="#dd88ef"/></svg>Crypto Wallet</div>
  <div class="abs cat" style="left:572px;top:55px;width:96px;height:98px">
    <svg viewBox="0 0 26 26"><path d="M3 10 13 4l10 6z" fill="#dd88ef"/><path d="M6 11v8M10.5 11v8M15.5 11v8M20 11v8" stroke="#dd88ef" stroke-width="2"/><rect x="3" y="20" width="20" height="2.5" fill="#dd88ef"/></svg>Bank Account</div>
  <div class="abs see-all">See all<svg width="12" height="8" viewBox="0 0 12 8"><path d="M0 0h12L6 8z" fill="#6c2488"/></svg></div>
  <div class="abs promo" role="img" aria-label="Cyber security banner with padlock, key and circuit artwork"></div>
  <div class="abs promo-dots"><i></i><i></i><i></i></div>
</section>

<section class="abs toolbar">
  <div class="abs tabs"><div class="on">Quick Tools</div><span>Tags</span></div>
  <div class="abs search-zone">
    <div class="abs search">Search for saved Passwords
      <svg width="16" height="16" viewBox="0 0 16 16"><circle cx="6.5" cy="6.5" r="5" fill="none" stroke="#888" stroke-width="1.6"/><path d="M10 10l4.5 4.5" stroke="#888" stroke-width="1.6"/></svg></div>
    <svg class="abs" style="left:271px;top:33px" width="14" height="10" viewBox="0 0 14 10"><path d="M0 1h14M3 5h8M5.5 9h3" stroke="#888" stroke-width="1.4"/></svg>
  </div>
  <div class="abs add-btn">
    <svg width="20" height="20" viewBox="0 0 20 20"><rect x="2" y="3" width="13" height="15" rx="1" fill="none" stroke="#fff" stroke-width="1.8"/><path d="M5 8h7M5 11.5h7M5 15h4M16.5 1v6M13.5 4h6" stroke="#fff" stroke-width="1.8"/></svg>
    Add New Passwords</div>
  <div class="abs dots" style="left:1164px;top:25px"><i></i><i></i><i></i></div>
</section>

<aside class="abs sidebar">
  <div class="abs tool first" style="top:3px"><svg viewBox="0 0 16 16"><rect x="2.5" y="7" width="11" height="8" rx="1" fill="#222"/><path d="M5 7V5a3 3 0 0 1 6 0v2" fill="none" stroke="#222" stroke-width="1.8"/></svg>Password Generator</div>
  <div class="abs tool" style="top:54px"><svg viewBox="0 0 16 16"><circle cx="8" cy="2.3" r="1.8" fill="#222"/><path d="M1 5h14v1.8h-5V16H8.6v-4H7.4v4H6V6.8H1z" fill="#222"/></svg>Password Health</div>
  <div class="abs tool" style="top:105px"><svg viewBox="0 0 16 16"><rect x="1" y="2" width="14" height="5" fill="#222"/><rect x="1" y="9" width="14" height="5" fill="#222"/><rect x="3" y="4" width="3" height="1.2" fill="#fff"/><rect x="3" y="11" width="3" height="1.2" fill="#fff"/></svg>Data Breach Scanner</div>
  <div class="abs tool" style="top:156px"><svg viewBox="0 0 16 16"><path d="M1 3h8l5 5-5 5H1l5-5z" fill="#222"/></svg>Emergency Access</div>
</aside>

<section class="abs table-head">
  <span class="cell" style="left:70px;top:14px">Title</span>
  <span class="cell" style="left:334px;top:14px">Last Used</span>
  <span class="cell" style="left:580px;top:14px">Action</span>
</section>

<div class="abs row" style="top:432px;height:50px;background:var(--row-grey)">
  <span class="cell" style="left:122px;top:17px">Postwell</span>
  <span class="cell" style="left:334px;top:17px">03.04.2022 - 2pm WAT</span>
  <svg class="cell" style="left:586px;top:21px" width="12" height="8" viewBox="0 0 12 8"><path d="M1 1l5 5 5-5" fill="none" stroke="#222" stroke-width="1.8"/></svg>
</div>
<div class="abs row" style="top:482px;height:50px;background:var(--white)">
  <div class="cell mark" style="left:73px;top:13px;background:var(--chirp)"></div>
  <span class="cell" style="left:122px;top:17px">chirpline</span>
  <span class="cell" style="left:334px;top:17px">03.04.2022 - 2pm WAT</span>
  <svg class="cell" style="left:586px;top:21px" width="12" height="8" viewBox="0 0 12 8"><path d="M1 1l5 5 5-5" fill="none" stroke="#222" stroke-width="1.8"/></svg>
</div>
<div class="abs row" style="top:532px;height:98px;background:var(--row-grey)">
  <div class="cell mark" style="left:73px;top:13px;background:var(--friend)"></div>
  <span class="cell" style="left:122px;top:17px;font-weight:700">Friendora</span>
  <span class="cell" style="left:334px;top:17px">03.04.2022 - 2pm WAT</span>
  <svg class="cell" style="left:586px;top:21px" width="12" height="8" viewBox="0 0 12 8"><path d="M1 7l5-5 5 5" fill="none" stroke="#222" stroke-width="1.8"/></svg>
  <div class="cell btn" style="left:587px;top:50px;width:98px;background:var(--lilac-btn)">Copy Details</div>
  <div class="cell btn" style="left:692px;top:50px;width:68px;background:var(--danger);color:var(--white)">Delete</div>
  <div class="cell btn" style="left:767px;top:50px;width:107px;background:var(--black);color:var(--white)">Edit/Add more</div>
</div>

<div class="abs view-menu">
  <div class="abs view-item" style="top:20px;color:var(--plum)"><svg width="20" height="14" viewBox="0 0 20 14"><path d="M0 1h3M6 1h14M0 7h3M6 7h14M0 13h3M6 13h14" stroke="#5b1a70" stroke-width="2"/></svg>List View</div>
  <div class="abs" style="left:13px;top:53px;width:112px;height:1px;background:var(--rule)"></div>
  <div class="abs view-item" style="top:67px;color:#aaa"><svg width="18" height="18" viewBox="0 0 18 18"><g fill="none" stroke="#aaa" stroke-width="1.6"><rect x="1" y="1" width="6" height="6"/><rect x="11" y="1" width="6" height="6"/><rect x="1" y="11" width="6" height="6"/><rect x="11" y="11" width="6" height="6"/></g></svg>Grid View</div>
</div>
</body>
</html>
```